New Business Card Design Project

The legal name of the company is TTTolvane, we also refer to it as simply Tolvane or you could also use the initials TTT...... please feel creative.
Excellent design.
On the second side, if you could image North and South America on each drop of water ... it almost looks like that now.
The website is www.tttolvane.com
Attached is another card with the required information; no addresses.

Industry/Entity Type

Legal

```html
<!DOCTYPE html>
<html lang="en">
<head>
<meta charset="utf-8">
<title>TTTolvane – Business Card</title>
<link rel="stylesheet" href="https://fonts.googleapis.com/css2?family=Montserrat:wght@800&family=Oxanium:wght@300;400&display=swap">
<style>
  :root {
    --page: #ffffff;
    --teal-deep: #0b3a48;
    --teal-mid: #1c8fb0;
    --teal-bright: #3fc6e6;
    --teal-light: #bfeefa;
    --band: rgba(10, 20, 24, 0.78);
    --url-green: #dcf08c;
    --panel: rgba(236, 240, 244, 0.86);
    --ink: #5b5d60;
    --icon-box: #5e5f61;
    --icon-line: #ffffff;
  }
  * { margin: 0; padding: 0; box-sizing: border-box; }
  html, body {
    width: 1063px; height: 1200px; overflow: hidden;
    background: var(--page);
  }
  .canvas { position: relative; width: 1063px; height: 1200px; }

  .card { position: absolute; overflow: hidden; }
  .card--front { left: 53px; top: 8px; width: 952px; height: 582px; }
  .card--back  { left: 48px; top: 601px; width: 960px; height: 596px; }

  .card__art {
    position: absolute; inset: 0;
    background:
      radial-gradient(circle at 82% 12%, var(--teal-light) 0%, rgba(191,238,250,0) 32%),
      radial-gradient(circle at 20% 55%, var(--teal-bright) 0%, rgba(63,198,230,0) 36%),
      radial-gradient(circle at 60% 78%, var(--teal-bright) 0%, rgba(63,198,230,0) 30%),
      radial-gradient(circle at 92% 70%, var(--teal-mid) 0%, rgba(28,143,176,0) 30%),
      linear-gradient(135deg, var(--teal-deep) 0%, var(--teal-mid) 55%, var(--teal-bright) 100%);
  }

  .card__band {
    position: absolute; left: 67px; right: 0; top: 250px; height: 80px;
    background: linear-gradient(90deg, rgba(10,20,24,0) 0%, var(--band) 10%, var(--band) 90%, rgba(10,20,24,0.55) 100%);
  }
  .card__url {
    position: absolute; left: 0; right: 0; top: 272px;
    text-align: center;
    font-family: "Oxanium", sans-serif; font-weight: 400;
    font-size: 27px; letter-spacing: 3px;
    color: var(--url-green);
  }

  .panel {
    position: absolute; left: 55px; top: 17px; width: 657px; height: 557px;
    background: var(--panel);
  }
  .company {
    position: absolute; left: 0; right: 0; top: 80px;
    text-align: center;
    font-family: "Montserrat", sans-serif; font-weight: 800;
    font-size: 30px; line-height: 40px; letter-spacing: 2.5px;
    color: var(--ink); text-transform: uppercase;
  }
  .person { position: absolute; left: 0; right: 0; top: 195px; text-align: center; color: var(--ink); }
  .person__name { font-family: "Oxanium", sans-serif; font-weight: 300; font-size: 29px; letter-spacing: 2px; }
  .person__role { font-family: "Oxanium", sans-serif; font-weight: 400; font-size: 21px; letter-spacing: 1.5px; margin-top: 2px; }

  .contact { position: absolute; left: 60px; display: flex; align-items: center; }
  .contact__icon { width: 67px; height: 47px; background: var(--icon-box); flex: none; }
  .contact__icon svg { display: block; width: 67px; height: 47px; }
  .contact__text {
    margin-left: 24px;
    font-family: "Oxanium", sans-serif; font-weight: 300;
    font-size: 27px; letter-spacing: 2.5px; line-height: 35px;
    color: var(--ink);
  }
  .contact--email { top: 307px; }
  .contact--web   { top: 370px; }
  .contact--phone { top: 433px; align-items: flex-start; }
  .contact--phone .contact__text { margin-top: -10px; }
</style>
</head>
<body>
<main class="canvas">

  <section class="card card--front">
    <div class="card__art" role="img" aria-label="Glowing teal water drops, each holding a globe of the world"></div>
    <div class="card__band"></div>
    <p class="card__url">www.tttolvane.com</p>
  </section>

  <section class="card card--back">
    <div class="card__art" role="img" aria-label="Glowing teal water drops with the Americas on a globe"></div>
    <div class="panel">
      <h1 class="company">Tolvane<br>TTTolvane SA, LLC</h1>

      <div class="person">
        <p class="person__name">Leon Varda</p>
        <p class="person__role">Managing Director</p>
      </div>

      <div class="contact contact--email">
        <span class="contact__icon">
          <svg viewBox="0 0 67 47" fill="none" stroke="var(--icon-line)" stroke-width="2.5">
            <rect x="14" y="10" width="39" height="27"/>
            <path d="M14 10 L33.5 26 L53 10 M14 37 L28 22 M53 37 L39 22"/>
          </svg>
        </span>
        <span class="contact__text">lva@tttolvane.com</span>
      </div>

      <div class="contact contact--web">
        <span class="contact__icon">
          <svg viewBox="0 0 67 47" fill="none" stroke="var(--icon-line)" stroke-width="2.5">
            <circle cx="33.5" cy="23.5" r="16"/>
            <ellipse cx="33.5" cy="23.5" rx="7" ry="16"/>
            <path d="M17.5 23.5 H49.5 M20 15 H47 M20 32 H47"/>
          </svg>
        </span>
        <span class="contact__text">www.tttolvane.com</span>
      </div>

      <div class="contact contact--phone">
        <span class="contact__icon">
          <svg viewBox="0 0 67 47" fill="none" stroke="var(--icon-line)" stroke-width="2.5" stroke-linejoin="round">
            <path d="M24 9 L30 9 L32 17 L28 20 C30 26 34 30 40 32 L43 28 L51 30 L51 36 C51 38 49 40 46 39 C33 37 25 29 22 15 C21 11 22 9 24 9 Z"/>
          </svg>
        </span>
        <span class="contact__text">USA: +1(305) 555 0148<br>GUATEMALA: +502 5550 3927</span>
      </div>
    </div>
  </section>

</main>
</body>
</html>
```